The Drifters

Amber Hawks Productions is looking for their theatrical poster for their film 'THE DRIFTERS'... It is a zombie appocalypse action film made in NSW Australia. See their facebook page www.facebook.com/THEDRIFTERSFILM...
Updates
Project Deadline Extended
Reason: i have decided to EXTEND the deadline for 5 more days, as there are some really talented artists reviewing their submissions for us... Thank you to all...
Please review the new uploaded images you may or may not want to use to revierw your submissions
Logo Text
Amber Hawks Productions
Look and feel
Each slider illustrates characteristics of the customer's brand and the style your logo design should communicate.

```html
<!DOCTYPE html>
<html lang="en">
<head>
<meta charset="utf-8">
<title>The Drifters – Theatrical Poster</title>
<link rel="stylesheet" href="https://fonts.googleapis.com/css2?family=Rubik+Dirt&family=Oswald:wght@400;500&display=swap">
<style>
  :root {
    --backdrop: #e9e8e6;
    --poster-black: #050302;
    --sky-deep: #7a0202;
    --sky-red: #b20a05;
    --sky-fire: #e8420c;
    --sun-glow: #ffd23a;
    --title-ink: #0a0403;
    --cast-gold: #f0a64a;
    --star-white: #f4f0ea;
  }
  * { box-sizing: border-box; margin: 0; padding: 0; }
  html, body {
    width: 1200px;
    height: 1148px;
    overflow: hidden;
    background: var(--backdrop);
  }
  .poster {
    position: absolute;
    left: 250px;
    top: 54px;
    width: 700px;
    height: 1040px;
    background: var(--poster-black);
  }
  .poster__scene {
    position: absolute;
    left: 38px;
    top: 44px;
    width: 624px;
    height: 850px;
    border-radius: 14px 22px 10px 18px;
    background:
      radial-gradient(ellipse 55% 40% at 82% 70%, var(--sun-glow) 0%, #ffa11e 25%, rgba(232,66,12,0.6) 55%, rgba(232,66,12,0) 80%),
      linear-gradient(180deg, var(--sky-deep) 0%, var(--sky-red) 45%, var(--sky-fire) 75%, #3a0503 92%, var(--poster-black) 100%);
  }
  .poster__title {
    position: absolute;
    left: 0;
    top: 190px;
    width: 700px;
    text-align: center;
    font-family: "Rubik Dirt", system-ui, sans-serif;
    color: var(--title-ink);
    line-height: 0.85;
  }
  .poster__title-the {
    display: block;
    font-size: 96px;
    margin-right: 110px;
  }
  .poster__title-main {
    display: block;
    font-size: 118px;
    letter-spacing: -2px;
  }
  .poster__tagline {
    position: absolute;
    top: 418px;
    left: 0;
    width: 700px;
    text-align: center;
    font-family: "Oswald", sans-serif;
    font-size: 11px;
    letter-spacing: 0.5px;
    color: var(--title-ink);
  }
  .poster__cast {
    position: absolute;
    left: 0;
    top: 930px;
    width: 700px;
    display: flex;
    justify-content: center;
    align-items: center;
    gap: 16px;
    font-family: "Oswald", sans-serif;
    font-weight: 400;
    font-size: 21px;
    color: var(--cast-gold);
    text-transform: uppercase;
    letter-spacing: -0.3px;
  }
  .poster__cast-star { color: var(--star-white); font-size: 16px; }
</style>
</head>
<body>
  <main class="poster">
    <div class="poster__scene" role="img" aria-label="Silhouettes of zombies walking against a blood-red sunset sky with a glowing sun at the lower right"></div>
    <h1 class="poster__title">
      <span class="poster__title-the">THE</span>
      <span class="poster__title-main">DRIFTERS</span>
    </h1>
    <p class="poster__tagline">BEFORE THEY FIND A CURE...THEY HAVE TO SURVIVE...</p>
    <p class="poster__cast">
      <span>Declan Hartley</span><span class="poster__cast-star">★</span>
      <span>Marco Venetti</span><span class="poster__cast-star">★</span>
      <span>Sophie Larkin</span><span class="poster__cast-star">★</span>
      <span>Reid Thomas</span>
    </p>
  </main>
</body>
</html>
```